Design clean technology service-based company website

Hello, We are looking to reskin our company website. We are an environmental inspection company and test for Asbestos, Lead and Mold along with other contaminants. People depend on the results to be accurate and fast. We are regulated by the EPA and State regulations. We work a lot with business to business and business to customer. We are wanting to make our new presentation to be modern and easy for customers to interact with us, understand our process and services while providing valuable environmental informational resource and updates. We are a technology based company and will be providing instantaneous results as reports come in for the customers. We are needing good calls to action on the site to direct them to setup a new inspection. Each user will have a backend access to their job information with invoices, reports, status, etc. We have developed software to be able to proved these reports and want to look the part.

My current website is www.trypelmarix.com

Helllo we are wanting to make sure we have good time to select the right website for us and also have the additional time to select other pages of the website. We have received great designs and have consolidated our requests into a document for the next set of iterations.

Target Market(s)

Home Owners, Contractors, Engineers, Real Estate Agents, Building Owners, Insurance Adjusters

Industry/Entity Type

Environmental Consultant

Number of Pages Required

5+ page

Font styles to use
Sans Serif

Colors
0355a3
9bcb3c
7f7f7f
f5f5f5
000000

Requirements
Must have
• Use our existing logo to design around
• The layouts look good in mobile mode for understanding and selecting services and signing up
• Clean Modern Layout
• Have all pages on the website have a similar layout and feel
• Clearly communicate services along with bundle service packages
• Detail the customer journey with graphic design
• Great call to actions to either schedule inspection online, call, text, chat
Nice to have
• Have an interactive graphic for where to test for lead, asbestos and mold.
• I like the barney kolts top order line bar - see attached
• Have clear question and answer page layouts for asbestos, lead and mold
• Show Company reviews
• Have clear Resources pages for all types of contaminants
Should not have
• My current website is www.trypelmarix.com

```html
<!DOCTYPE html>
<html lang="en">
<head>
<meta charset="utf-8">
<title>Trypelmarix Environmental Inspections</title>
<link href="https://fonts.googleapis.com/css2?family=Open+Sans:wght@400;600;700&display=swap" rel="stylesheet">
<style>
:root{
  --blue:#0355a3;
  --green:#52c41a;
  --black:#000000;
  --ink:#111111;
  --grey:#7f7f7f;
  --light:#e0e0e0;
  --paper:#f5f5f5;
  --white:#ffffff;
  --footer:#2a2a2a;
  --badge:#b8b8b8;
}
*{margin:0;padding:0;box-sizing:border-box}
html,body{width:1200px;height:2609px;overflow:hidden}
body{position:relative;font-family:"Open Sans",Arial,sans-serif;color:var(--ink);background:var(--white)}
.abs{position:absolute}

/* top bar */
.topbar{left:0;top:0;width:1200px;height:28px;background:var(--black)}
.social{display:flex;gap:6px;left:99px;top:6px}
.social span{width:16px;height:16px;background:var(--white);border-radius:2px}
.topbar-note{right:99px;top:5px;color:var(--white);font-size:13px;font-weight:600}

/* header */
.brand-box{left:0;top:28px;width:358px;height:122px;background:var(--white)}
.brand{left:99px;top:52px;display:flex;align-items:center;gap:10px}
.brand-dot{width:18px;height:18px;border-radius:50%;background:var(--green)}
.brand-name{font-size:34px;font-weight:700;color:var(--green);line-height:1}
.brand-sub{left:127px;top:92px;font-size:10px;letter-spacing:1.5px;color:var(--ink)}
.order-bar{left:358px;top:28px;width:842px;height:76px;background:var(--blue)}
.order-title{left:414px;top:34px;color:var(--white);font-size:21px;font-weight:700;line-height:30px;text-align:center}
.login{left:577px;top:62px;color:var(--white);font-size:17px}
.field-label{color:var(--white);font-size:11px;font-weight:600}
.street{left:690px;top:64px;width:171px;height:25px;background:var(--white);border:1px solid #999;font-size:11px;color:var(--grey);padding:4px 5px}
.opt{height:24px;background:var(--black);color:var(--white);font-size:12px;font-weight:600;display:flex;align-items:center;justify-content:center}
.nav{left:358px;top:104px;width:842px;height:35px;background:var(--green)}
.nav a{position:absolute;top:0;height:35px;line-height:35px;font-size:15px;color:var(--ink);text-decoration:none;font-weight:600}
.nav .current{background:var(--black);color:var(--white);padding:0 9px}

/* hero */
.hero{left:0;top:150px;width:1200px;height:375px;background:linear-gradient(120deg,#3a3f44 0%,#6c7176 45%,#8a8f93 60%,#4a4d50 100%)}
.hero-card{left:144px;top:261px;width:357px;height:167px;background:rgba(20,20,20,.65)}
.hero-title{left:169px;top:282px;color:var(--white);font-size:21px;font-weight:700;line-height:38px;letter-spacing:.5px}
.call-btn{background:var(--blue);color:var(--white);font-size:16px;display:flex;align-items:center;justify-content:center}

/* services */
.svc-green{left:0;top:525px;width:437px;height:311px;background:var(--green);color:var(--white);text-align:center}
.svc-green h2{position:absolute;left:0;width:520px;top:36px;font-size:25px;font-weight:700}
.svc-green .big{position:absolute;left:0;width:520px;top:96px;font-size:56px;font-weight:700}
.svc-green .sub{position:absolute;left:0;width:520px;top:178px;font-size:26px}
.svc-blue{left:437px;top:525px;width:763px;height:311px;background:var(--blue)}
.svc-item{width:190px;text-align:center;color:var(--white);font-size:20px;line-height:25px}

/* how it works */
.how{left:0;top:836px;width:1200px;height:515px;background:var(--light)}
.how-label{left:99px;top:918px;font-size:22px;font-weight:700}
.how-title{left:99px;top:987px;font-size:25px;font-weight:700}
.how-copy{left:99px;top:1040px;width:540px;font-size:16px;line-height:25px;color:#222}
.how-copy p{margin-bottom:25px}
.read-more{left:99px;top:1266px;width:92px;height:25px;background:var(--green);color:var(--white);font-size:15px;display:flex;align-items:center;justify-content:center}
.video{left:729px;top:976px;width:370px;height:273px;background:#000}
.video-frame{left:755px;top:1008px;width:318px;height:190px;background:radial-gradient(circle at 50% 55%,#c98f84,#7c4b43 70%,#3a2522)}

/* construction band */
.build{left:0;top:1351px;width:1200px;height:336px;background:linear-gradient(180deg,#4e4e4e,#6a6a6a 55%,#565656)}
.build h3{position:absolute;left:101px;top:72px;color:var(--white);font-size:24px;font-weight:700}
.build p{position:absolute;left:101px;top:148px;width:720px;color:var(--white);font-size:25px;line-height:37px}

/* accreditations */
.badges{left:0;top:1687px;width:1200px;height:374px;background:var(--white)}
.badge{background:var(--badge)}

/* footer */
.footer{left:0;top:2061px;width:1200px;height:488px;background:var(--footer)}
.f-head{font-size:20px;font-weight:700;color:var(--white)}
.f-rule{width:70px;height:3px;background:var(--blue)}
.f-item{left:135px;font-size:16px;color:var(--white);display:flex;align-items:center}
.f-icon{left:99px}
.map{left:456px;top:2158px;width:236px;height:282px;background:linear-gradient(135deg,#eef0ec,#dfe3dc 60%,#f1e2b0)}
.input{left:836px;width:265px;background:var(--white);color:#aaa;font-size:14px;padding:8px 6px}
.submit{left:838px;top:2454px;width:68px;height:23px;background:var(--green);color:var(--white);font-size:15px;font-weight:700;display:flex;align-items:center;justify-content:center}
.f-brand{left:99px;top:2384px;display:flex;align-items:center;gap:8px}
.f-brand .brand-name{font-size:30px}
.f-nav{left:0;width:1200px;top:2522px;text-align:center;font-size:15px;color:var(--white)}
.f-nav span{margin:0 9px}
.bottombar{left:0;top:2549px;width:1200px;height:60px;background:var(--black)}
.copyright{left:99px;top:2570px;color:var(--white);font-size:13px}
.social-foot{right:99px;top:2572px;display:flex;gap:6px}
.social-foot span{width:18px;height:18px;background:var(--white);border-radius:2px}
</style>
</head>
<body>

<!-- top bar -->
<div class="abs topbar"></div>
<div class="abs social"><span></span><span></span><span></span><span></span></div>
<div class="abs topbar-note">Fully Accredited. 24/7 Same Day Response.</div>

<!-- header -->
<div class="abs brand-box"></div>
<div class="abs brand"><span class="brand-dot"></span><span class="brand-name">Trypelmarix</span></div>
<div class="abs brand-sub">ENVIRONMENTAL INSPECTIONS</div>

<div class="abs order-bar"></div>
<div class="abs order-title">ORDER<br>ONLINE</div>
<div class="abs login">Login</div>
<div class="abs field-label" style="left:690px;top:42px">Start an order</div>
<div class="abs street">Enter street address</div>
<div class="abs field-label" style="left:907px;top:41px">Choose Option</div>
<div class="abs opt" style="left:906px;top:65px;width:78px">Delivery</div>
<div class="abs opt" style="left:1009px;top:65px;width:76px">Pickup</div>

<nav class="abs nav">
  <a class="current" style="left:40px">HOME</a>
  <a style="left:127px">OUR SERVICES</a>
  <a style="left:268px">RESOURCES</a>
  <a style="left:392px">BLOG</a>
  <a style="left:470px">Q&amp;A</a>
  <a style="left:539px">REVIEWS</a>
  <a style="left:642px">CONNECT</a>
</nav>

<!-- hero -->
<div class="abs hero" role="img" aria-label="Inspector in a white protective suit testing a construction site"></div>
<div class="abs hero-card"></div>
<div class="abs hero-title">FAST, DEPENDABLE RESULTS,<br>WHEN IT MATTERS THE MOST</div>
<div class="abs call-btn" style="left:230px;top:367px;width:184px;height:35px">CALL-US 555-210-4478</div>

<!-- services -->
<section class="abs svc-green">
  <h2>OUR SERVICES</h2>
  <div class="big">24/7/365</div>
  <div class="sub">Same Day Service</div>
</section>
<div class="abs svc-blue"></div>
<svg class="abs" style="left:437px;top:525px" width="763" height="311" viewBox="437 525 763 311">
  <g fill="#fff" stroke="#000" stroke-width="3">
    <circle cx="616" cy="647" r="68"/>
    <circle cx="803" cy="647" r="68"/>
    <circle cx="991" cy="647" r="68"/>
  </g>
  <g fill="#000">
    <rect x="576" y="616" width="22" height="52"/>
    <rect x="600" y="600" width="24" height="68"/>
    <rect x="626" y="628" width="14" height="40"/>
    <polygon points="640,650 650,640 660,650 660,668 640,668"/>
  </g>
  <g fill="#fff">
    <rect x="581" y="624" width="5" height="6"/><rect x="589" y="624" width="5" height="6"/>
    <rect x="581" y="638" width="5" height="6"/><rect x="589" y="638" width="5" height="6"/>
    <rect x="605" y="610" width="5" height="6"/><rect x="614" y="610" width="5" height="6"/>
    <rect x="605" y="626" width="5" height="6"/><rect x="614" y="626" width="5" height="6"/>
    <rect x="605" y="642" width="5" height="6"/><rect x="614" y="642" width="5" height="6"/>
  </g>
  <polygon points="803,610 760,648 770,648 770,680 836,680 836,648 846,648" fill="#000"/>
  <rect x="790" y="652" width="12" height="12" fill="#fff"/>
  <rect x="808" y="652" width="12" height="12" fill="#fff"/>
  <path d="M970 640 a21 21 0 0 1 42 0 z" fill="#000"/>
  <rect x="966" y="638" width="50" height="6" fill="#000"/>
  <circle cx="991" cy="654" r="12" fill="#000"/>
  <path d="M958 688 q0-22 33-22 q33 0 33 22 z" fill="#000"/>
</svg>
<div class="abs svc-item" style="left:521px;top:748px">Commercial<br>Services</div>
<div class="abs svc-item" style="left:708px;top:748px">Residental<br>Services</div>
<div class="abs svc-item" style="left:896px;top:748px">Home Owner<br>Services</div>

<!-- how it works -->
<section class="abs how"></section>
<h2 class="abs how-label">HOW IT WORKS</h2>
<h3 class="abs how-title">Environmental Testing Evolved</h3>
<div class="abs how-copy">
  <p>Trypelmarix grew up in the rough and tumble disaster restoration industry. Time and time again, we saw projects small and large brought to a stand-still to await environmental testing and results.</p>
  <p>First, we had to know when it’s prudent or even required by law to test for asbestos, lead-based paint, mold or other contaminants. Then we had to track down reliable testing companies, facilities or equipment.</p>
</div>
<div class="abs read-more">Read More</div>
<div class="abs video"></div>
<div class="abs video-frame" role="img" aria-label="Embedded video about the symptoms of mold exposure"></div>

<!-- construction band -->
<section class="abs build" role="img" aria-label="Textured grey background of insulation material">
  <h3>NEW CONSTRUCTION PROJECT ?</h3>
  <p>Let us start you in the right direction with our certified asbestos inspections ...Residential, commercial, schools, governmental properties, multi-family and more.A</p>
</section>
<div class="abs call-btn" style="left:890px;top:1631px;width:183px;height:33px">CALL-US 555-210-4478</div>

<!-- accreditations -->
<div class="abs badges"></div>
<div class="abs badge" style="left:110px;top:1741px;width:300px;height:115px;border-radius:10px"></div>
<div class="abs badge" style="left:466px;top:1756px;width:431px;height:87px;border-radius:6px"></div>
<div class="abs badge" style="left:939px;top:1725px;width:150px;height:150px;border-radius:50%"></div>
<div class="abs badge" style="left:266px;top:1906px;width:329px;height:120px;border-radius:6px"></div>
<div class="abs badge" style="left:621px;top:1908px;width:290px;height:113px;border-radius:6px"></div>

<!-- footer -->
<footer class="abs footer"></footer>
<div class="abs f-head" style="left:99px;top:2086px">Contact Us</div>
<div class="abs f-rule" style="left:99px;top:2119px"></div>
<div class="abs f-head" style="left:450px;top:2086px">Location</div>
<div class="abs f-rule" style="left:450px;top:2119px"></div>
<div class="abs f-head" style="left:836px;top:2086px">Feedback</div>
<div class="abs f-rule" style="left:836px;top:2119px"></div>

<svg class="abs f-icon" style="top:2157px" width="26" height="20" viewBox="0 0 26 20"><rect x="1" y="1" width="24" height="18" fill="none" stroke="#52c41a" stroke-width="2"/><polyline points="1,1 13,11 25,1" fill="none" stroke="#52c41a" stroke-width="2"/></svg>
<div class="abs f-item" style="top:2156px">hello@trypelmarix.com</div>
<svg class="abs f-icon" style="top:2210px" width="22" height="24" viewBox="0 0 22 24"><path d="M5 1 l5 0 l2 6 l-3 3 q2 5 7 7 l3-3 l6 2 l0 5 q-1 3-4 3 q-17-2-19-19 q0-3 3-4z" fill="#52c41a"/></svg>
<div class="abs f-item" style="top:2211px">555-210-4478</div>
<svg class="abs f-icon" style="top:2261px" width="20" height="26" viewBox="0 0 20 26"><path d="M10 0 a9 9 0 0 1 9 9 c0 7-9 17-9 17 s-9-10-9-17 a9 9 0 0 1 9-9z" fill="#52c41a"/><circle cx="10" cy="9" r="3.5" fill="#2a2a2a"/></svg>
<div class="abs f-item" style="top:2264px">Unit 12, Brookfield</div>

<div class="abs f-brand"><span class="brand-dot"></span><span class="brand-name">Trypelmarix</span></div>

<div class="abs map" role="img" aria-label="Street map showing the office location"></div>

<div class="abs input" style="top:2156px;height:39px">Name</div>
<div class="abs input" style="top:2214px;height:38px">Email</div>
<div class="abs input" style="top:2271px;height:38px">Mobile</div>
<div class="abs input" style="top:2328px;height:114px">Message</div>
<div class="abs submit">Submit</div>

<div class="abs f-nav">HOME<span>|</span>OUR SERVICES<span>|</span>RESOURCES<span>|</span>BLOG<span>|</span>Q&amp;A<span>|</span>REVIEWS<span>|</span>CONNECT</div>

<div class="abs bottombar"></div>
<div class="abs copyright">©2018 Trypelmarix Environmental Inspections</div>
<div class="abs social-foot"><span></span><span></span><span></span><span></span></div>

</body>
</html>
```